4月11日公示の青嶺市議会議員選挙に立候補予定です
新人ですが、組織もないので、浮動票を獲得できる目立つポスターをお願いいします
◎公選法のポスターサイズ
42センチ×30センチ 縦・横は自由です
◎入れてもらいたい内容
青嶺市議会議員候補者
藤岡 さとえ
掲示責任者:藤岡里恵
印刷社:西原グラフ印刷株式会社東京都足立区鷺沼台町2-16

◎入れてもらいたいキャッチコピー
まもれ子供の命 元稲見町役場職員 2016民主党「市民ゼミナール」出身
決定後の微調整をお願いすると思いますが、ご理解いただける方

```html
<!DOCTYPE html>
<html lang="ja">
<head>
<meta charset="utf-8">
<title>藤岡 さとえ 選挙ポスター</title>
<link rel="stylesheet" href="https://fonts.googleapis.com/css2?family=M+PLUS+Rounded+1c:wght@700;800;900&family=Noto+Sans+JP:wght@500;700;900&display=swap">
<style>
  :root {
    --blue: #1f5cb8;
    --green: #6dbf45;
    --green-soft: #8ccf5e;
    --ink: #1a1a1a;
    --paper: #ffffff;
    --suit: #2a2f3a;
    --skin: #d9a98a;
  }
  html, body {
    margin: 0;
    padding: 0;
    width: 857px;
    height: 1200px;
    overflow: hidden;
    background: var(--paper);
  }
  .poster {
    position: relative;
    width: 857px;
    height: 1200px;
    overflow: hidden;
    background: var(--paper);
    font-family: "Noto Sans JP", sans-serif;
    color: var(--ink);
  }
  .decor { position: absolute; inset: 0; }
  .name {
    margin: 0;
    font-family: "M PLUS Rounded 1c", sans-serif;
    font-weight: 900;
    color: var(--blue);
  }
  .name > span {
    position: absolute;
    display: block;
    line-height: 1;
    white-space: nowrap;
  }
  .name-family {
    left: 40px;
    top: 24px;
    font-size: 250px;
    letter-spacing: 10px;
  }
  .name-reading {
    left: 540px;
    top: 270px;
    font-size: 30px;
    font-weight: 800;
    letter-spacing: 3px;
  }
  .name-given {
    left: 44px;
    top: 312px;
    font-size: 186px;
    letter-spacing: 10px;
  }
  .credentials {
    position: absolute;
    left: 22px;
    top: 514px;
    margin: 0;
    font-weight: 700;
    font-size: 24px;
    line-height: 1;
    color: var(--green);
    white-space: nowrap;
  }
  .credentials span + span { margin-left: 14px; }
  .portrait {
    position: absolute;
    left: 380px;
    top: 610px;
    width: 477px;
    height: 590px;
    border-radius: 48% 48% 0 0 / 30% 30% 0 0;
    background: linear-gradient(180deg, var(--skin) 0%, var(--skin) 45%, var(--suit) 62%, var(--suit) 100%);
  }
  .slogan {
    position: absolute;
    left: 58px;
    top: 600px;
    margin: 0;
    font-weight: 900;
    font-size: 64px;
    line-height: 1.25;
    letter-spacing: 2px;
  }
  .office {
    position: absolute;
    left: 40px;
    top: 982px;
    margin: 0;
    font-weight: 900;
    font-size: 40px;
    line-height: 1.22;
  }
  .imprint {
    position: absolute;
    left: 40px;
    top: 1130px;
    margin: 0;
    font-size: 11px;
    line-height: 1.5;
    font-weight: 500;
    color: #555;
  }
</style>
</head>
<body>
<main class="poster">
  <svg class="decor" width="857" height="1200" viewBox="0 0 857 1200" aria-hidden="true">
    <path class="leaf" d="M720 0 L857 0 L857 140 C800 140 735 95 720 0 Z" fill="var(--green-soft)"/>
    <circle class="backdrop-circle" cx="620" cy="965" r="400" fill="var(--green)"/>
  </svg>

  <h1 class="name">
    <span class="name-family">藤岡</span>
    <span class="name-reading">ふじおか</span>
    <span class="name-given">さとえ</span>
  </h1>

  <p class="credentials"><span>●元稲見町役場職員</span><span>●2016共進党「市民ゼミナール」出身</span></p>

  <div class="portrait" role="img" aria-label="候補者の上半身の写真（スーツ姿で笑顔）"></div>

  <p class="slogan">守れ!<br>子供の命</p>

  <p class="office">青嶺市議会議員<br>選挙候補者</p>

  <p class="imprint">掲示責任者：藤岡里恵<br>印刷者：西原グラフ印刷株式会社 東京都足立区鷺沼台町2-16</p>
</main>
</body>
</html>
```